Breakthrough Sports Drink Needs a Label Design

Using the logo provided, we need a label design for a new sports drink company called 'Vorna'. We have developed a clear and light, protein-infused beverage for elite athletes.

We would like to label to use a similar color scheme as the logo provided. It needs to portray a refreshing, healthy feel but also needs to reflect the functional aspects of the drink.

The label needs to clearly include the phrases: "18 grams of protein", "For the Elite Athlete" and " "2:1 ratio of carbs to protein "

Target Market(s)

College Athletes

Industry/Entity Type

It Company

Requirements
Must have
• Should be based on the logo provided and include the phrases:
• 18g of Protein
• For The Elite Athlete
• 2:1 Ratio of Carbs to Protein

```html
<!DOCTYPE html>
<html lang="en">
<head>
<meta charset="utf-8">
<title>Vorna Athletic Recovery – Label</title>
<link rel="stylesheet" href="https://fonts.googleapis.com/css2?family=Michroma&display=swap">
<style>
  :root {
    --stage: #e4e9f0;
    --facet-light: #c9ccd3;
    --facet-mid: #8c93a3;
    --facet-dark: #4b5366;
    --panel: #ffffff;
    --ink: #1e2129;
    --ink-soft: #3a3f4c;
    --accent: #2c2a70;
    --tagline: #2d3f92;
    --headline: #ffffff;
  }
  html, body {
    margin: 0;
    padding: 0;
    width: 925px;
    height: 1200px;
    overflow: hidden;
    background: var(--stage);
  }
  .canvas {
    width: 925px;
    height: 1200px;
    display: flex;
    align-items: center;
    justify-content: center;
  }
  .label {
    width: 640px;
    height: 900px;
    display: block;
    box-shadow: 0 10px 30px rgba(40, 50, 70, 0.18);
  }
  .label text {
    font-family: "Michroma", sans-serif;
  }
  .brand-name { fill: var(--ink); font-size: 38px; }
  .brand-tagline { fill: var(--tagline); font-size: 11px; letter-spacing: 1.5px; }
  .kicker { fill: var(--ink-soft); font-size: 15px; }
  .headline { fill: var(--headline); font-size: 50px; }
  .figure { fill: var(--accent); font-size: 30px; }
  .claim { fill: var(--ink); font-size: 17px; }
</style>
</head>
<body>
<main class="canvas">
  <svg class="label" viewBox="0 0 590 830" xmlns="http://www.w3.org/2000/svg">
    <defs>
      <linearGradient id="facetTone" x1="0" y1="0" x2="1" y2="1">
        <stop offset="0" stop-color="var(--facet-mid)"/>
        <stop offset="0.35" stop-color="var(--facet-light)"/>
        <stop offset="0.7" stop-color="var(--facet-mid)"/>
        <stop offset="1" stop-color="var(--facet-dark)"/>
      </linearGradient>
    </defs>

    <rect class="facet-field" width="590" height="830" fill="url(#facetTone)"
          role="img" aria-label="Angular grey-blue faceted background pattern"/>

    <polygon class="panel panel-brand" fill="var(--panel)"
             points="396,0 590,0 590,178 342,96 296,60"/>
    <polygon class="panel panel-ratio" fill="var(--panel)"
             points="0,525 115,548 195,660 118,780 0,770"/>
    <polygon class="panel panel-protein" fill="var(--panel)"
             points="346,830 426,700 590,680 590,830"/>

    <g class="brand">
      <text class="brand-name" x="352" y="88">VORNA</text>
      <text class="brand-tagline" x="352" y="110">ATHLETIC RECOVERY</text>
    </g>

    <g class="title">
      <text class="kicker" x="62" y="290">FOR THE</text>
      <text class="headline" x="60" y="345">ELITE</text>
      <text class="headline" x="60" y="412">ATHLETE</text>
    </g>

    <g class="claim-ratio">
      <text class="figure" x="12" y="632">2:1</text>
      <text class="claim" x="92" y="630">ratio</text>
      <text class="claim" x="12" y="656">of carbs</text>
      <text class="claim" x="12" y="682">to protein</text>
    </g>

    <g class="claim-protein">
      <text class="figure" x="396" y="762">18</text>
      <text class="claim" x="470" y="760">grams</text>
      <text class="claim" x="396" y="792">of protein</text>
    </g>
  </svg>
</main>
</body>
</html>
```